Web site design for Brivolt Software (www.brivoltsoftware-example.com)

Need the design as well as the html for the website. The brief is given in the attached file.
If possible, would like to use pencil sketches instead of images to give a unique look to the site.
Target Market(s)
small Software product companies
Industry/Entity Type
Software
Coding
Coded - Design and coding required
Number of Pages Required
5+ page

```html
<!DOCTYPE html>
<html lang="en">
<head>
<meta charset="utf-8">
<title>Brivolt Software – About us</title>
<link href="https://fonts.googleapis.com/css2?family=Montserrat:wght@600;700;800&family=Roboto:wght@400;500&display=swap" rel="stylesheet">
<style>
:root{
  --yellow:#f9b90f;
  --dark:#1c1c1c;
  --bar:#222222;
  --text:#3a3a3a;
  --muted:#555555;
  --white:#ffffff;
  --rule:#e2e2e2;
}
*{margin:0;padding:0;box-sizing:border-box}
html,body{width:990px;height:1200px;overflow:hidden;background:var(--white)}
body{position:relative;font-family:'Roboto',sans-serif;color:var(--text)}
.abs{position:absolute;white-space:nowrap}

.topbar{position:absolute;left:0;top:0;width:990px;height:31px;background:var(--bar);color:var(--white);font-size:10px;font-weight:500}
.topbar .item{position:absolute;top:9px;display:flex;align-items:center;gap:5px}
.topbar .links{position:absolute;top:9px;right:81px;display:flex;gap:21px}

.header{position:absolute;left:0;top:31px;width:990px;height:83px;background:var(--white)}
.logo{position:absolute;left:77px;top:24px;display:flex;align-items:center;gap:9px}
.logo .mark{width:31px;height:34px;background:var(--yellow);border-radius:6px}
.logo .name{font-family:'Montserrat',sans-serif;font-weight:700;font-size:24px;color:var(--dark)}
.nav{position:absolute;top:33px;font-size:12.5px;color:#444}

.hero{position:absolute;left:0;top:114px;width:990px;height:192px;background:linear-gradient(100deg,#4d443c 0%,#7b6a58 35%,#a3917c 55%,#6f6356 80%,#57504a 100%)}
.hero .crumb{position:absolute;left:77px;top:45px;font-size:13px;color:var(--white)}
.hero h1{position:absolute;left:77px;top:71px;font-family:'Montserrat',sans-serif;font-weight:700;font-size:29px;color:var(--white)}
.hero .quote{position:absolute;left:77px;top:121px;font-size:13px;font-weight:500;color:var(--white)}

.about h2{position:absolute;left:77px;top:352px;font-family:'Montserrat',sans-serif;font-weight:700;font-size:28px;color:var(--dark)}
.yline{position:absolute;height:3px;background:var(--yellow)}
.about p{position:absolute;left:77px;font-size:13.5px;line-height:23px;color:var(--text);width:600px}
.art{position:absolute;left:725px;top:350px;width:138px;height:205px;background:radial-gradient(circle at 50% 45%,#ffffff 0%,#c6d7e2 30%,#9fb5c6 50%,#e9eff3 75%,#fbfcfd 100%)}

.section-title{position:absolute;font-family:'Montserrat',sans-serif;font-weight:800;font-size:35px;color:#111}
.line{position:absolute;font-size:11.5px;color:var(--muted);line-height:21px}
.divider{position:absolute;left:497px;top:590px;width:1px;height:263px;background:var(--rule)}

.footer{position:absolute;left:0;top:881px;width:990px;height:319px;background:radial-gradient(ellipse at 60% 30%,#2c2c2c 0%,#1b1b1b 70%)}
.footer .label{position:absolute;font-size:8.5px;font-weight:500;color:var(--white)}
.footer .head{position:absolute;font-family:'Montserrat',sans-serif;font-weight:700;font-size:13px;color:var(--white)}
.footer .txt{position:absolute;font-size:9px;line-height:16px;color:var(--white);font-weight:500}
.footer .row{position:absolute;display:flex;align-items:center;gap:6px;font-size:9.5px;color:var(--white);font-weight:500}
.map{position:absolute;left:312px;top:132px;width:174px;height:86px;background:linear-gradient(90deg,#6a6a6a,#8c8c8c,#6a6a6a);opacity:.8;border-radius:8px}
.social{position:absolute;top:185px;width:27px;height:27px;border-radius:50%;background:var(--yellow)}
</style>
</head>
<body>

<div class="topbar">
  <div class="item" style="left:77px">
    <svg width="10" height="10" viewBox="0 0 10 10"><circle cx="5" cy="5" r="4" fill="none" stroke="#fff" stroke-width="1.1"/><path d="M5 2.6V5h2" stroke="#fff" stroke-width="1.1" fill="none"/></svg>
    Working hours: Mon - Sat 8.00 - 18.00
  </div>
  <div class="item" style="left:269px">
    <svg width="9" height="11" viewBox="0 0 9 11"><rect x="1" y="0.6" width="7" height="9.8" rx="1" fill="none" stroke="#fff" stroke-width="1.1"/><circle cx="4.5" cy="8.3" r=".8" fill="#fff"/></svg>
    Call Us: (+1) 555 610-4402
  </div>
  <div class="links"><span>Case Studise</span><span>Work With us</span><span>Partners</span><span>Stories</span><span>Blog</span><span>Contact</span></div>
</div>

<div class="header">
  <div class="logo"><span class="mark"></span><span class="name">Brivolt</span></div>
  <span class="nav abs" style="left:315px">Home</span>
  <span class="nav abs" style="left:385px">About us</span>
  <span class="nav abs" style="left:471px">Services</span>
  <span class="nav abs" style="left:552px">Expertise</span>
  <span class="nav abs" style="left:638px">Engagement Models</span>
  <span class="nav abs" style="left:789px">Aggile</span>
  <span class="nav abs" style="left:860px">Accolades</span>
</div>

<div class="hero" role="img" aria-label="Close-up photo of welding sparks in a workshop">
  <div class="crumb">HOME</div>
  <h1>About us</h1>
  <div class="quote">If I have seen further than others, it is by standing upon the shoulders of giants. Elden Marr</div>
</div>

<section class="about">
  <h2>About Us</h2>
  <div class="yline" style="left:77px;top:398px;width:55px"></div>
  <p style="top:415px">We are seasoned programmers, interested in the science as well as the craft of programming.</p>
  <p style="top:452px">We need to put high res black and white photos of Tarvesh – followed by a paragraph about Tarvesh<br>Ditto with Lokan and RJ</p>
  <div class="art" role="img" aria-label="Abstract iridescent swirl artwork in pale blue tones"></div>
</section>

<h2 class="section-title" style="left:70px;top:590px">Vision</h2>
<div class="line abs" style="left:70px;top:649px">To build a world class software product and product services company</div>

<h2 class="section-title" style="left:70px;top:728px">Mission</h2>
<div class="line abs" style="left:70px;top:786px">To develop software products that can evolve elegantly.</div>
<div class="line abs" style="left:70px;top:819px">To take an architecture driven route for developing products.</div>

<div class="divider"></div>

<h2 class="section-title" style="left:508px;top:590px">Values</h2>
<div class="line abs" style="left:508px;top:649px">To deal with customers, share holders and employees with highest standard of<br>business ethics</div>
<div class="line abs" style="left:508px;top:702px">To maintain transparency and continuous communication across company and<br>with stakeholders</div>
<div class="line abs" style="left:508px;top:755px">To generate value for all stakeholders</div>
<div class="line abs" style="left:508px;top:788px">To be an organization driven by architecture</div>

<footer class="footer">
  <div class="label" style="left:118px;top:81px">BALTIMORE</div>
  <div class="head" style="left:118px;top:95px">Headquarters</div>
  <div class="yline" style="left:118px;top:117px;width:30px;height:2px"></div>
  <div class="txt" style="left:118px;top:123px">Interactively coordinate proactive “outside<br>the box” thinking.</div>
  <div class="row" style="left:118px;top:164px">
    <svg width="11" height="11" viewBox="0 0 11 11"><path d="M2.4 1l2 2-1.2 1.4c.7 1.4 1.7 2.4 3.1 3.1L7.7 6.3l2 2-1.3 1.6C4.7 9.6 1.2 6.2 1 2.2z" fill="#fff"/></svg>
    +1 555 7148203</div>
  <div class="row" style="left:118px;top:183px">
    <svg width="11" height="11" viewBox="0 0 11 11"><circle cx="3.5" cy="3.5" r="2.2" fill="none" stroke="#fff" stroke-width="1.3"/><circle cx="7.5" cy="7.5" r="2.2" fill="none" stroke="#fff" stroke-width="1.3"/></svg>
    www.brivoltsoftware-example.com</div>
  <div class="row" style="left:118px;top:202px">
    <svg width="12" height="10" viewBox="0 0 12 10"><rect x="0.5" y="0.5" width="11" height="9" rx="1" fill="#fff"/><path d="M1 1l5 4 5-4" stroke="#1b1b1b" stroke-width="1" fill="none"/></svg>
    hello@brivoltsoftware-example.com</div>

  <div class="label" style="left:312px;top:81px">LOCATIONS</div>
  <div class="head" style="left:312px;top:95px">We Are Everywhere</div>
  <div class="yline" style="left:312px;top:117px;width:30px;height:2px"></div>
  <div class="map" role="img" aria-label="Dotted world map with office locations marked"></div>

  <div class="label" style="left:505px;top:142px">OUR NETWORK</div>
  <div class="row" style="left:505px;top:162px"><svg width="8" height="10" viewBox="0 0 8 10"><path d="M4 10C1.5 6.5 0.5 5 0.5 3.5a3.5 3.5 0 017 0C7.5 5 6.5 6.5 4 10z" fill="#fff"/><circle cx="4" cy="3.5" r="1.2" fill="#1b1b1b"/></svg><span style="font-size:8px">Chicago: +1 555 3082 716</span></div>
  <div class="row" style="left:505px;top:180px"><svg width="8" height="10" viewBox="0 0 8 10"><path d="M4 10C1.5 6.5 0.5 5 0.5 3.5a3.5 3.5 0 017 0C7.5 5 6.5 6.5 4 10z" fill="#fff"/><circle cx="4" cy="3.5" r="1.2" fill="#1b1b1b"/></svg><span style="font-size:8px">Amsterdam: +1 555 6621 904</span></div>
  <div class="row" style="left:505px;top:198px"><svg width="8" height="10" viewBox="0 0 8 10"><path d="M4 10C1.5 6.5 0.5 5 0.5 3.5a3.5 3.5 0 017 0C7.5 5 6.5 6.5 4 10z" fill="#fff"/><circle cx="4" cy="3.5" r="1.2" fill="#1b1b1b"/></svg><span style="font-size:8px">Berlin: +1 555 418 2259</span></div>

  <div class="label" style="left:699px;top:81px">GET IN TOUCH</div>
  <div class="head" style="left:699px;top:95px">Follow Our Activity</div>
  <div class="yline" style="left:699px;top:117px;width:30px;height:2px"></div>
  <div class="txt" style="left:699px;top:123px">Interactively coordinate proactive e-<br>commerce via process-centric “outside the<br>box” thinking.</div>
  <span class="social" style="left:699px"></span>
  <span class="social" style="left:730px"></span>
  <span class="social" style="left:762px"></span>
  <span class="social" style="left:793px"></span>
</footer>

</body>
</html>
```